Allied Health Clinic needs catchy poster ad for lightbox

We need a catchy and effective poster designed for our retail lightbox which is in a busy corridor. We are a multi disciplinary sports injury clinic offering a range of allied health services. Established in 1999. We need people to understand our business identity and services clearly. I have come up with a very rough idea as far as what I think the copy should contain. The picture is an example of what image I am trying to convey to the potential client. I am not a designer clearly. We specialise in treating difficult problems.
Size of the poster is 451mm x 741mm at 300dpi. We will then blow the image up to double this size which will be good enough resolution for the printing.

Target Market(s)

White collar professionals - male and female, active 20-50 range

Industry/Entity Type

Healthcare

Font styles to use
Sans Serif

Requirements
Nice to have
• Easy to read, polished, nice tie in to my logo colours

```html
<!DOCTYPE html>
<html lang="en">
<head>
<meta charset="utf-8">
<title>Corefit Physiotherapy – Lightbox Poster</title>
<link rel="stylesheet" href="https://fonts.googleapis.com/css2?family=Source+Sans+3:wght@400;600;700&display=swap">
<style>
  :root {
    --green: #8cc63f;
    --dark: #4a4a4b;
    --ink: #3d3d3f;
    --blue: #4ea9e0;
    --white: #ffffff;
    --sky: #d8ecf8;
    --font: "Source Sans 3", sans-serif;
  }
  * { margin: 0; padding: 0; box-sizing: border-box; }
  html, body { width: 883px; height: 1200px; overflow: hidden; background: var(--white); }
  .poster {
    position: relative; width: 883px; height: 1200px; overflow: hidden;
    font-family: var(--font);
    background: linear-gradient(to bottom, var(--sky) 0, #f4f9fd 90px, var(--white) 200px);
  }
  .athlete-photo {
    position: absolute; left: 250px; top: 30px; width: 633px; height: 700px;
    background: radial-gradient(ellipse at 65% 45%, #c9cdd6 0%, #e4e6ec 45%, rgba(255,255,255,0) 72%);
  }
  .shapes { position: absolute; inset: 0; }
  .headline {
    position: absolute; left: 33px; top: 42px;
    font-weight: 700; font-size: 37px; line-height: 62px; color: var(--ink);
  }
  .headline .accent { color: var(--green); }
  .tagline {
    position: absolute; left: 33px; top: 190px;
    font-weight: 600; font-size: 26px; line-height: 44px; color: var(--blue);
  }
  .brand { position: absolute; left: 33px; top: 690px; }
  .brand-dot { width: 40px; height: 40px; border-radius: 50%; background: var(--green); margin-bottom: 10px; }
  .brand-name {
    font-weight: 600; font-size: 27px; line-height: 30px; color: var(--ink);
    letter-spacing: 1.5px; text-transform: uppercase;
  }
  .brand-sub {
    font-weight: 600; font-size: 15px; letter-spacing: 7px; color: var(--ink);
    text-transform: uppercase; margin-top: 2px;
  }
  .services-label {
    position: absolute; left: 490px; top: 837px; width: 393px; height: 40px;
    background: var(--green); border-radius: 14px 0 0 14px;
    color: var(--white); font-weight: 700; font-size: 24px;
    text-align: right; padding-right: 38px; line-height: 40px;
  }
  .services-list { position: absolute; right: 30px; top: 893px; list-style: none; }
  .services-list li {
    display: flex; justify-content: flex-end; align-items: center; gap: 16px;
    color: var(--white); font-weight: 600; font-size: 27px; height: 43px;
  }
  .services-list svg { width: 24px; height: 24px; }
  .lift-badge {
    position: absolute; left: 80px; top: 919px; width: 172px; height: 172px;
    border-radius: 50%; background: var(--blue); border: 3px solid var(--white);
    display: flex; align-items: center; justify-content: center; text-align: center;
    color: var(--white); font-weight: 700; font-size: 25px; line-height: 33px;
  }
  .footer {
    position: absolute; left: 0; bottom: 0; width: 883px; height: 81px;
    background: var(--green); display: flex; align-items: center;
    padding: 0 28px 0 33px; color: var(--white);
  }
  .phone { display: flex; align-items: center; gap: 14px; font-weight: 600; font-size: 40px; }
  .phone svg { width: 44px; height: 44px; }
  .website { margin-left: auto; font-weight: 600; font-size: 27px; }
</style>
</head>
<body>
<main class="poster">
  <div class="athlete-photo" role="img" aria-label="Photo of a footballer in a navy shirt and white shorts kicking a ball in mid-air"></div>

  <svg class="shapes" viewBox="0 0 883 1200" width="883" height="1200" aria-hidden="true">
    <path d="M0 394 C 110 610, 380 700, 883 762" fill="none" stroke="var(--green)" stroke-width="5"/>
    <path d="M0 929 C 200 820, 520 790, 883 783 L883 1200 L0 1200 Z" fill="var(--dark)"/>
    <path d="M0 929 C 200 820, 520 790, 883 783" fill="none" stroke="var(--green)" stroke-width="5"/>
  </svg>

  <h1 class="headline"><span class="accent">INJURY</span> EXPERTS<br>TRUSTED BY ATHLETES</h1>
  <p class="tagline">SUCCESSFULLY<br>TREATING DIFFICULT<br>INJURIES SINCE 1999</p>

  <div class="brand">
    <div class="brand-dot"></div>
    <div class="brand-name">Corefit Physiotherapy</div>
    <div class="brand-sub">&amp; Sports Injury Clinic</div>
  </div>

  <div class="services-label">SERVICES OFFERED</div>
  <ul class="services-list">
    <li>SPORT PHYSIOTHERAPY <svg viewBox="0 0 24 24"><circle cx="12" cy="12" r="12" fill="var(--green)"/><path d="M14 7 L9 12 L14 17" fill="none" stroke="var(--dark)" stroke-width="3"/></svg></li>
    <li>CHIROPRACTIC <svg viewBox="0 0 24 24"><circle cx="12" cy="12" r="12" fill="var(--green)"/><path d="M14 7 L9 12 L14 17" fill="none" stroke="var(--dark)" stroke-width="3"/></svg></li>
    <li>MASSAGE <svg viewBox="0 0 24 24"><circle cx="12" cy="12" r="12" fill="var(--green)"/><path d="M14 7 L9 12 L14 17" fill="none" stroke="var(--dark)" stroke-width="3"/></svg></li>
    <li>PODIATRY <svg viewBox="0 0 24 24"><circle cx="12" cy="12" r="12" fill="var(--green)"/><path d="M14 7 L9 12 L14 17" fill="none" stroke="var(--dark)" stroke-width="3"/></svg></li>
    <li>EXERCISE PHYSIOLOGY <svg viewBox="0 0 24 24"><circle cx="12" cy="12" r="12" fill="var(--green)"/><path d="M14 7 L9 12 L14 17" fill="none" stroke="var(--dark)" stroke-width="3"/></svg></li>
  </ul>

  <div class="lift-badge">TAKE<br>LIFTS TO<br>LEVEL 8</div>

  <footer class="footer">
    <div class="phone">
      <svg viewBox="0 0 44 44" aria-hidden="true"><circle cx="22" cy="22" r="19.5" fill="none" stroke="var(--white)" stroke-width="3"/><path d="M15 11 C12 13, 12 18, 16 24 C20 30, 25 33, 29 32 L31 29 L26 25 L24 27 C21 26, 18 22, 17 19 L19 17 L16 11 Z" fill="var(--white)"/></svg>
      <span>8123 4567</span>
    </div>
    <div class="website">corefitphysioclinic.com.au</div>
  </footer>
</main>
</body>
</html>
```